KEV.PRO- Darren Holcombe Fitness- needs a clever business card using the logo, name, info, contact

I need a business card designed for my Online Personal Training company called KEV.PRO, abbreviation for Darren Holcombe Fitness. My company focuses on coaching in personal health and personal growth to unleash your greatest potential. I would like to see designs that use my color scheme of a redish-orange (C:0,M:84,Y:100,K:0), grey, white, black, and my company font is OSWALD. The final design should communicate some aspects of design, health, motivation, growth, in some way. The logo is very important to the company and can be displayed in any of the colors previously mentioned. Must include the company name, my website: www.kev-pro.example , my email: dan@kev-pro.example

Target Market(s)

Personal health, fitness, general public, those who lack knowledge, awareness, and confidence in personal health

Industry/Entity Type

Personal Trainer

Font styles to use
Other font styles liked:
• OSWALD. (Bold, Regular, Light)

Colors
f37122
ffffff
9d9d9d
000000

Requirements
Must have
• Must include the logo, company name, my website: www.kev-pro.example , my email: dan@kev-pro.example
Nice to have
• Variations of the colors scheme of a redish-orange (C:0,M:84,Y:100,K:0), grey, white, black. Logo, card, or text can be in any of these colors.
• Possible quote like "Take control of your personal health to unleash your greatest potential" or "Unleashing your greatness first begins with fitness of the body and mind"

```html
<!DOCTYPE html>
<html lang="en">
<head>
<meta charset="utf-8">
<title>KEV.PRO Business Card</title>
<link href="https://fonts.googleapis.com/css2?family=Oswald:wght@300;400;700&family=Roboto+Mono:wght@700&display=swap" rel="stylesheet">
<style>
  :root {
    --orange: #ef5423;
    --ink: #3b2a24;
    --black: #000000;
    --white: #ffffff;
    --grey-bg: #6e6d70;
    --grey-photo-light: #9d9d9d;
    --grey-photo-dark: #2a2a2a;
  }
  * { margin: 0; padding: 0; box-sizing: border-box; }
  html, body { width: 1200px; height: 1200px; overflow: hidden; }
  body {
    background: var(--grey-bg);
    display: flex;
    flex-direction: column;
    align-items: center;
    justify-content: center;
    gap: 40px;
    font-family: 'Oswald', sans-serif;
  }
  .card {
    position: relative;
    width: 900px;
    height: 514px;
    overflow: hidden;
  }

  /* Front */
  .card-front { background: var(--orange); }
  .brand-block {
    position: absolute;
    top: 70px;
    right: 70px;
    text-align: left;
  }
  .brand-name {
    font-weight: 700;
    font-size: 112px;
    line-height: 0.95;
    letter-spacing: -1px;
  }
  .brand-tagline {
    font-weight: 300;
    font-size: 30px;
    line-height: 1.1;
    letter-spacing: -0.5px;
  }
  .card-front .brand-name,
  .card-front .brand-tagline { color: var(--ink); }

  .front-mark {
    position: absolute;
    left: 50%;
    top: 340px;
    transform: translateX(-50%);
    display: flex;
    align-items: center;
    gap: 18px;
  }
  .mark-dot {
    width: 34px;
    height: 34px;
    border-radius: 50%;
    background: var(--ink);
  }
  .mark-name {
    font-weight: 700;
    font-size: 64px;
    color: var(--ink);
    line-height: 1;
  }

  /* Back */
  .card-back { background: var(--black); }
  .athlete-photo {
    position: absolute;
    left: 0;
    top: 0;
    width: 560px;
    height: 100%;
    background:
      linear-gradient(90deg, rgba(0,0,0,0) 55%, var(--black) 100%),
      radial-gradient(ellipse at 45% 40%, var(--grey-photo-light) 0%, #5c5c5c 40%, var(--grey-photo-dark) 80%);
  }
  .quote {
    position: absolute;
    left: 60px;
    bottom: 60px;
    font-family: 'Roboto Mono', monospace;
    font-weight: 700;
    font-size: 30px;
    line-height: 1.7;
    letter-spacing: 3px;
    color: var(--white);
  }
  .card-back .brand-block { top: 60px; right: 90px; }
  .card-back .brand-name { color: var(--orange); }
  .card-back .brand-tagline { color: var(--white); }

  .contact-list {
    position: absolute;
    left: 560px;
    top: 270px;
    list-style: none;
  }
  .contact-item {
    display: flex;
    align-items: center;
    gap: 12px;
    font-family: 'Roboto Mono', monospace;
    font-weight: 700;
    font-size: 17px;
    letter-spacing: 1.5px;
    color: var(--white);
    margin-bottom: 12px;
  }
  .contact-icon { width: 18px; height: 18px; flex: none; }

  .back-mark {
    position: absolute;
    left: 640px;
    bottom: 70px;
    display: flex;
    align-items: center;
    gap: 10px;
  }
  .back-mark .mark-dot { width: 20px; height: 20px; background: var(--white); }
  .back-mark .mark-name { font-size: 32px; color: var(--white); }
</style>
</head>
<body>

  <section class="card card-front">
    <div class="brand-block">
      <div class="brand-name">KEV.PRO</div>
      <div class="brand-tagline">DARREN HOLCOMBE.FITNESS</div>
    </div>
    <div class="front-mark">
      <span class="mark-dot"></span>
      <span class="mark-name">KEV.PRO</span>
    </div>
  </section>

  <section class="card card-back">
    <div class="athlete-photo" role="img" aria-label="Black-and-white photo of a shirtless athlete wearing boxing gloves"></div>
    <p class="quote">“Take control of your<br>personal HEALTH to<br>unleash your<br>GREATEST potential”</p>

    <div class="brand-block">
      <div class="brand-name">KEV.PRO</div>
      <div class="brand-tagline">DARREN HOLCOMBE.FITNESS</div>
    </div>

    <ul class="contact-list">
      <li class="contact-item">
        <svg class="contact-icon" viewBox="0 0 18 18"><circle cx="9" cy="9" r="7.5" fill="none" stroke="#ef5423" stroke-width="2"/><path d="M1.5 9h15M9 1.5c3 3.5 3 11.5 0 15M9 1.5c-3 3.5-3 11.5 0 15" fill="none" stroke="#ef5423" stroke-width="1.5"/></svg>
        www.kev-pro.example
      </li>
      <li class="contact-item">
        <svg class="contact-icon" viewBox="0 0 18 18"><rect x="1" y="4" width="16" height="11" fill="#ef5423"/><path d="M1 4l8 6 8-6" fill="none" stroke="#000" stroke-width="1.5"/></svg>
        dan@kev-pro.example
      </li>
      <li class="contact-item">
        <svg class="contact-icon" viewBox="0 0 18 18"><circle cx="9" cy="9" r="7" fill="#ef5423"/></svg>
        www.social.example/kev.pro
      </li>
    </ul>

    <div class="back-mark">
      <span class="mark-dot"></span>
      <span class="mark-name">KEV.PRO</span>
    </div>
  </section>

</body>
</html>
```